Vira Glow - Letter Head

My company is a residential and commercial cleaning company , which is located in Abu Dhabi, UAE.
I am looking for a creative letterhead reflects the professional and reflects professionalism and send the feeling of relax and comfort.
The color which will be used it has to be selected carefully in prospective of colors psychological effects, so every color to be used should be for a reason.
Also, reflecting my company colors in an attractive way.
Regarding the information which it should contains, it has to show the address, contacts , telephones an, email address and website.
Also, my company logo is attached

```html
<!DOCTYPE html>
<html lang="en">
<head>
<meta charset="utf-8">
<title>Vira Glow — Stationery Set</title>
<link rel="stylesheet" href="https://fonts.googleapis.com/css2?family=Source+Sans+3:wght@400;600;700&family=Source+Serif+4:wght@400&display=swap">
<style>
:root{
  --stage:#e5e5e5;
  --paper:#ffffff;
  --brand-blue:#1d6fc1;
  --brand-green:#8dc63f;
  --ink:#555a60;
  --ink-soft:#7a7f85;
  --field:#e9eaec;
  --window:#e8e8e8;
  --shadow:0 1px 4px rgba(0,0,0,.22);
}
*{box-sizing:border-box;margin:0;padding:0}
html,body{width:1200px;height:524px;overflow:hidden}
body{background:var(--stage);position:relative;font-family:"Source Sans 3",Arial,sans-serif;color:var(--ink)}
.sheet{position:absolute;background:var(--paper);box-shadow:var(--shadow);overflow:hidden}

/* brand name block (replaces mark) */
.brand{position:absolute;display:flex;align-items:center;gap:5px;font-weight:700;color:var(--brand-blue);white-space:nowrap}
.brand .dot{border-radius:50%;background:var(--brand-green);flex:none}

/* envelope back */
.envelope-back{left:38px;top:63px;width:362px;height:182px}
.envelope-back .flap{position:absolute;left:0;top:0;width:362px;height:58px}
.envelope-back .brand{left:50%;top:18px;transform:translateX(-50%);font-size:13px;color:var(--paper)}
.envelope-back .brand .dot{width:12px;height:12px}

/* envelope front */
.envelope-front{left:38px;top:282px;width:362px;height:180px}
.envelope-front .brand{left:16px;top:28px;font-size:21px}
.envelope-front .brand .dot{width:20px;height:20px}
.envelope-front .return-address{position:absolute;left:17px;top:91px;font-size:10.5px;line-height:13px;color:var(--brand-blue);font-weight:600}
.envelope-front .address-window{position:absolute;left:256px;top:74px;width:86px;height:51px;border-radius:5px;background:var(--window)}
.wave{position:absolute;left:0;bottom:0;display:block}

/* letter sheets */
.letterhead{left:434px;top:18px;width:368px;height:492px}
.fax-sheet{left:817px;top:18px;width:346px;height:492px}
.letterhead .brand{left:50%;top:44px;transform:translateX(-50%);font-size:24px}
.fax-sheet .brand{left:50%;top:38px;transform:translateX(-50%);font-size:24px}
.brand-lg .dot{width:22px;height:22px}

.copy{position:absolute;font-size:6.4px;line-height:8.5px;color:var(--ink)}
.copy p{margin-bottom:5px}
.copy .serif{font-family:"Source Serif 4",Georgia,serif;font-size:6.3px}
.letterhead .salutation{position:absolute;left:27px;top:106px;font-size:6.6px;line-height:8.4px}
.letterhead .copy{left:27px;top:141px;width:322px}
.fax-sheet .copy{left:22px;top:223px;width:306px}

.signature{position:absolute;width:62px;height:26px;border-radius:14px;background:linear-gradient(90deg,#eeeeee,#e2e3e5)}
.letterhead .signature{left:27px;top:360px}
.fax-sheet .signature{left:28px;top:368px}

.contacts{position:absolute;top:414px;font-size:8.6px;line-height:12.6px;color:var(--ink)}
.contacts li{list-style:none;display:flex;align-items:center;gap:5px}
.contacts svg{width:7px;height:7px;flex:none}
.letterhead .contacts-phone{left:31px}
.letterhead .contacts-web{left:216px}
.fax-sheet .contacts-phone{left:31px}
.fax-sheet .contacts-web{left:218px}

.footer-address{position:absolute;right:22px;bottom:10px;font-size:8.8px;font-weight:600;color:var(--paper);white-space:nowrap}
.fax-sheet .footer-address{right:20px}

/* fax header table */
.fax-fields{position:absolute;left:22px;top:97px;width:304px;border-collapse:separate;border-spacing:2px 1px;font-size:6px;color:var(--ink)}
.fax-fields td{height:15px;background:var(--field);padding:0 4px}
.fax-fields .label{width:38px}
.fax-options{position:absolute;left:25px;top:165px;width:300px;display:flex;justify-content:space-between;font-size:5.4px;color:var(--ink)}
.fax-options span{display:flex;align-items:center;gap:4px}
.fax-options span::before{content:"";width:6px;height:6px;border:1px solid #9a9ea3;background:var(--paper)}
</style>
</head>
<body>

<!-- Envelope, back -->
<section class="sheet envelope-back" aria-label="Envelope back">
  <svg class="flap" viewBox="0 0 362 58" preserveAspectRatio="none" aria-hidden="true">
    <path d="M0 0H362V44C300 50 250 56 181 56S62 50 0 44Z" fill="var(--brand-blue)"/>
  </svg>
  <div class="brand"><span class="dot"></span>Vira Glow</div>
</section>

<!-- Envelope, front -->
<section class="sheet envelope-front" aria-label="Envelope front">
  <div class="brand"><span class="dot"></span>Vira Glow</div>
  <p class="return-address">27 Palm Crescent,<br>Al Reem, Abu Dhabi</p>
  <div class="address-window"></div>
  <svg class="wave" width="362" height="42" viewBox="0 0 362 42" aria-hidden="true">
    <path d="M0 16C70 2 150 2 230 14S330 22 362 8V42H0Z" fill="var(--brand-green)"/>
    <path d="M0 22C70 10 150 10 230 20S330 28 362 14V42H0Z" fill="var(--paper)"/>
    <path d="M0 27C80 16 160 18 240 26S330 30 362 20V42H0Z" fill="var(--brand-blue)"/>
  </svg>
</section>

<!-- Letterhead -->
<section class="sheet letterhead" aria-label="Letterhead">
  <div class="brand brand-lg"><span class="dot"></span>Vira Glow</div>
  <p class="salutation">Lpsum, lorem<br>dolor sit amet<br>Lorem, dummy text</p>
  <div class="copy">
    <p>Lorem ipsum dolor sit amet, consetetur sadipscing elitr, sed diam nonumy eirmod tempor invidunt ut labore et dolore magna aliquyam erat, sed diam voluptua. At vero eos et accusam et justo duo dolores et ea rebum. Stet clita kasd gubergren, no sea takimata sanctus est Lorem ipsum dolor sit</p>
    <p>Lorem ipsum dolor sit amet, consetetur sadipscing elitr, sed diam nonumy eirmod tempor invidunt ut labore et dolore magna aliquyam erat, sed diam voluptua. At vero eos et accusam et justo duo dolores et ea rebum. Stet clita kasd gubergren, no sea takimata sanctus est Lorem ipsum dolor sit amet. Lorem ipsum dolor sit amet, consetetur sadipscing elitr, sed diam nonumy eirmod tempor invidunt ut labore et dolore magna aliquyam erat, sed diam voluptua. At vero eos et accusam et justo duo dolores et ea rebum. Stet clita kasd gubergren, no sea takimata sanctus est Lorem ipsum dolor sit amet. Lorem ipsum dolor sit amet, consetetur sadipscing elitr, sed diam nonumy eirmod tempor invidunt ut labore et dolore magna aliquyam erat, sed diam voluptua. At vero eos et accusam et justo duo dolores et ea rebum. Stet clita kasd gubergren, no sea takimata sanctus est</p>
    <p class="serif">Duis autem vel eum iriure dolor in hendrerit in vulputate velit esse molestie consequat, vel illum dolore eu feugiat nulla facilisis at vero eros et accumsan et iusto odio dignissim qui blandit praesent luptatum zzril delenit augue duis dolore te feugait nulla facilisi. Lorem ipsum dolor sit amet, consectetuer adipiscing elit, sed diam nonummy nibh euismod tincidunt ut laoreet dolore magna aliquam erat volutpat.</p>
    <p class="serif">Ut wisi enim ad minim veniam, quis nostrud exerci tation ullamcorper suscipit lobortis nisl ut aliquip ex ea commodo consequat. Duis autem vel eum iriure dolor in hendrerit in vulputate velit esse molestie consequat, vel illum dolore eu feugiat nulla facilisis at vero eros et accumsan et iusto odio dignissim qui blandit praesent luptatum zzril delenit augue duis dolore te feugait nulla facilisi.</p>
  </div>
  <div class="signature" role="img" aria-label="Handwritten signature of the sender"></div>
  <ul class="contacts contacts-phone">
    <li><svg viewBox="0 0 10 10"><path d="M2 1l2 2-1 1.5c.6 1.2 1.4 2 2.5 2.5L7 6l2 2-1.5 1.5C4.5 9 1 5.5.5 2.5Z" fill="var(--brand-blue)"/></svg>(555) 214-3870</li>
    <li><svg viewBox="0 0 10 10"><rect x="1" y="4" width="8" height="5" rx="1" fill="var(--brand-blue)"/><rect x="3" y="1" width="4" height="3" fill="var(--brand-blue)"/></svg>(555) 214-3871</li>
    <li><svg viewBox="0 0 10 10"><rect x="2.5" y="0.5" width="5" height="9" rx="1" fill="var(--brand-blue)"/><rect x="3.5" y="1.8" width="3" height="5.5" fill="#fff"/></svg>(555) 308-1942</li>
  </ul>
  <ul class="contacts contacts-web">
    <li><svg viewBox="0 0 10 10"><rect x="0.5" y="2" width="9" height="6.5" rx="1" fill="var(--brand-blue)"/><path d="M1 2.6L5 5.8 9 2.6" stroke="#fff" fill="none"/></svg>hello@viraglow.com</li>
    <li><svg viewBox="0 0 10 10"><circle cx="5" cy="5" r="4.5" fill="var(--brand-blue)"/><path d="M.5 5h9M5 .5c-2 2.5-2 6.5 0 9M5 .5c2 2.5 2 6.5 0 9" stroke="#fff" stroke-width=".6" fill="none"/></svg>www.viraglow.com</li>
  </ul>
  <svg class="wave" width="368" height="48" viewBox="0 0 368 48" aria-hidden="true">
    <path d="M0 16C80 2 160 4 240 14S330 20 368 6V48H0Z" fill="var(--brand-green)"/>
    <path d="M0 22C80 10 160 12 240 20S330 26 368 13V48H0Z" fill="var(--paper)"/>
    <path d="M0 26C80 16 160 18 240 25S330 30 368 18V48H0Z" fill="var(--brand-blue)"/>
  </svg>
  <p class="footer-address">27 Palm Crescent, Al Reem, Abu Dhabi</p>
</section>

<!-- Fax cover sheet -->
<section class="sheet fax-sheet" aria-label="Fax cover sheet">
  <div class="brand brand-lg"><span class="dot"></span>Vira Glow</div>
  <table class="fax-fields">
    <tr><td class="label">To</td><td></td><td class="label">From</td><td></td></tr>
    <tr><td class="label">FAX</td><td></td><td class="label">Pages</td><td></td></tr>
    <tr><td class="label">Phone</td><td></td><td class="label">Date</td><td></td></tr>
    <tr><td class="label">Re</td><td></td><td class="label">CC</td><td></td></tr>
  </table>
  <div class="fax-options">
    <span>Urgent</span><span>For Review</span><span>Please comment</span><span>Please reply</span><span>Please recycle</span>
  </div>
  <div class="copy">
    <p>Lorem ipsum dolor sit amet, consetetur sadipscing elitr, sed diam nonumy eirmod tempor invidunt ut labore et dolore magna aliquyam erat, sed diam voluptua. At vero eos et accusam et justo duo dolores et ea rebum. Stet clita kasd gubergren, no sea takimata sanctus est Lorem ipsum dolor sit</p>
    <p>Lorem ipsum dolor sit amet, consetetur sadipscing elitr, sed diam nonumy eirmod tempor invidunt ut labore et dolore magna aliquyam erat, sed diam voluptua. At vero eos et accusam et justo duo dolores et ea rebum. Stet clita kasd gubergren, no sea takimata sanctus est Lorem ipsum dolor sit amet. Lorem ipsum dolor sit amet, consetetur sadipscing elitr, sed diam nonumy eirmod tempor invidunt ut labore et dolore magna aliquyam erat, sed diam voluptua. At vero eos et accusam et justo duo dolores et ea rebum. Stet clita kasd gubergren, no sea takimata sanctus est Lorem ipsum dolor sit amet. Lorem ipsum dolor sit amet, consetetur sadipscing elitr, sed diam nonumy eirmod tempor invidunt ut labore et dolore magna aliquyam erat, sed diam voluptua. At vero eos et accusam et justo duo dolores et ea rebum. Stet clita kasd gubergren, no sea takimata sanctus est</p>
    <p class="serif">Duis autem vel eum iriure dolor in hendrerit in vulputate velit esse molestie consequat, vel illum dolore eu feugiat nulla facilisis at vero eros et accumsan et iusto odio dignissim qui blandit praesent luptatum zzril delenit augue duis dolore te feugait nulla facilisi. Lorem ipsum dolor sit amet, consectetuer adipiscing elit, sed diam nonummy nibh euismod tincidunt ut laoreet dolore magna aliquam erat volutpat.</p>
  </div>
  <div class="signature" role="img" aria-label="Handwritten signature of the sender"></div>
  <ul class="contacts contacts-phone">
    <li><svg viewBox="0 0 10 10"><path d="M2 1l2 2-1 1.5c.6 1.2 1.4 2 2.5 2.5L7 6l2 2-1.5 1.5C4.5 9 1 5.5.5 2.5Z" fill="var(--brand-blue)"/></svg>(555) 214-3870</li>
    <li><svg viewBox="0 0 10 10"><rect x="1" y="4" width="8" height="5" rx="1" fill="var(--brand-blue)"/><rect x="3" y="1" width="4" height="3" fill="var(--brand-blue)"/></svg>(555) 214-3871</li>
    <li><svg viewBox="0 0 10 10"><rect x="2.5" y="0.5" width="5" height="9" rx="1" fill="var(--brand-blue)"/><rect x="3.5" y="1.8" width="3" height="5.5" fill="#fff"/></svg>(555) 308-1942</li>
  </ul>
  <ul class="contacts contacts-web">
    <li><svg viewBox="0 0 10 10"><rect x="0.5" y="2" width="9" height="6.5" rx="1" fill="var(--brand-blue)"/><path d="M1 2.6L5 5.8 9 2.6" stroke="#fff" fill="none"/></svg>hello@viraglow.com</li>
    <li><svg viewBox="0 0 10 10"><circle cx="5" cy="5" r="4.5" fill="var(--brand-blue)"/><path d="M.5 5h9M5 .5c-2 2.5-2 6.5 0 9M5 .5c2 2.5 2 6.5 0 9" stroke="#fff" stroke-width=".6" fill="none"/></svg>www.viraglow.com</li>
  </ul>
  <svg class="wave" width="346" height="48" viewBox="0 0 346 48" aria-hidden="true">
    <path d="M0 16C75 2 150 4 225 14S310 20 346 6V48H0Z" fill="var(--brand-green)"/>
    <path d="M0 22C75 10 150 12 225 20S310 26 346 13V48H0Z" fill="var(--paper)"/>
    <path d="M0 26C75 16 150 18 225 25S310 30 346 18V48H0Z" fill="var(--brand-blue)"/>
  </svg>
  <p class="footer-address">27 Palm Crescent, Al Reem, Abu Dhabi</p>
</section>

</body>
</html>
```